the halvorsen group premier division

design a DL A4 tri fold brochure to reflect our creative landscape business
my web site www.thehalvorsengroup.com.au
has all the information needed
i will also be updating the website to be more updated and creative design

```html
<!DOCTYPE html>
<html lang="en">
<head>
<meta charset="utf-8">
<title>The Halvorsen Group – Landscape Consulting and Design</title>
<link href="https://fonts.googleapis.com/css2?family=Raleway:wght@200;300&family=Roboto+Condensed:wght@300&display=swap" rel="stylesheet">
<style>
  :root {
    --paper: #ffffff;
    --ink: #222222;
    --body-ink: #474747;
    --accent: #f29a1d;
    --photo-dusk: #7f907f;
    --photo-foliage: #93a84e;
    --photo-deck: #8a6b52;
    --photo-wall: #c8c6b6;
    --photo-paving: #7a7b74;
    --photo-bluestone: #686a66;
    --photo-entrance: #9c9d98;
    --photo-pool: #5e8e85;
    --photo-lawn: #6e9a4b;
    --photo-evening: #4f6e78;
    --photo-timber: #8b7260;
  }
  * { margin: 0; padding: 0; box-sizing: border-box; }
  html, body { width: 1200px; height: 848px; overflow: hidden; background: var(--paper); }
  .spread { position: relative; width: 1200px; height: 848px; background: var(--paper); }
  .photo-strip { position: absolute; left: 0; width: 1200px; height: 129px; display: block; }
  .photo-strip--top { top: 0; }
  .photo-strip--bottom { top: 719px; }
  .display-title {
    position: absolute;
    font-family: 'Raleway', sans-serif;
    font-weight: 200;
    font-size: 43px;
    letter-spacing: 4.2px;
    color: var(--ink);
    line-height: 1;
    white-space: nowrap;
  }
  .display-title--main { left: 36px; top: 126px; }
  .display-title--lifestyle { right: 38px; top: 684px; }
  .service-column { position: absolute; top: 186px; width: 340px; }
  .service-column--consult { left: 40px; }
  .service-column--earthwork { left: 420px; }
  .service-column--install { left: 820px; }
  .service-heading {
    font-family: 'Raleway', sans-serif;
    font-weight: 300;
    font-size: 20px;
    color: var(--accent);
    margin-bottom: 16px;
    white-space: nowrap;
  }
  .service-text {
    font-family: 'Roboto Condensed', sans-serif;
    font-weight: 300;
    font-size: 15px;
    line-height: 18.75px;
    color: var(--body-ink);
    text-align: justify;
  }
  .service-text + .service-text { margin-top: 18.75px; }
  .capability-list {
    list-style: none;
    display: grid;
    grid-template-columns: 112px 1fr;
    grid-auto-flow: column;
    grid-template-rows: repeat(9, auto);
    font-family: 'Roboto Condensed', sans-serif;
    font-weight: 300;
    font-size: 15px;
    line-height: 18.75px;
    color: var(--body-ink);
  }
  .capability-list li { position: relative; padding-left: 20px; }
  .capability-list li::before { content: "•"; position: absolute; left: 0; }
  .capability-list .capability--second { grid-column: 2; }
  .materials { margin-top: 18.75px; }
</style>
</head>
<body>
<main class="spread">
  <svg class="photo-strip photo-strip--top" viewBox="0 0 1280 138" preserveAspectRatio="none">
    <g role="img" aria-label="Photo: grand rendered house at dusk with clipped hedges"><polygon points="0,0 214,0 208,138 0,138" fill="var(--photo-dusk)"/></g>
    <g role="img" aria-label="Photo: close-up of a green grassy plant"><polygon points="222,0 426,0 420,138 216,138" fill="var(--photo-foliage)"/></g>
    <g role="img" aria-label="Photo: timber deck with steps and rendered garden walls"><polygon points="436,0 642,0 636,138 430,138" fill="var(--photo-deck)"/></g>
    <g role="img" aria-label="Photo: built-in bench with red cushions beneath climbing plants"><polygon points="651,0 856,0 850,138 645,138" fill="var(--photo-wall)"/></g>
    <g role="img" aria-label="Photo: paved courtyard beside a glass-fronted house"><polygon points="864,0 1066,0 1060,138 858,138" fill="var(--photo-paving)"/></g>
    <g role="img" aria-label="Photo: white outdoor table set on bluestone paving"><polygon points="1074,0 1280,0 1280,138 1068,138" fill="var(--photo-bluestone)"/></g>
  </svg>

  <h1 class="display-title display-title--main">LANDSCAPE CONSULTING AND DESIGN</h1>

  <section class="service-column service-column--consult">
    <h2 class="service-heading">CONSULTATION AND DESIGN</h2>
    <p class="service-text">Our landscape designers will begin by discussing your needs and look at your property and setting to create a concept where all attributes are considered from the land itself, design style, the elements and impact, through to lifestyle, and functionality and of course budget.</p>
    <p class="service-text">Whether it be new or existing, Ben Torrance can provide advice on materials, earth and irrigation, planting, features and so with only quality and longevity in mind.</p>
    <p class="service-text">You may also opt for a digital interpretation of your design, at an additional cost, to help you visualise the transformation and how the design fits in with its surrounds.</p>
    <p class="service-text">If you have something particular in mind or uncertain about, Ben would be happy to assist.</p>
  </section>

  <section class="service-column service-column--earthwork">
    <h2 class="service-heading">EARTHWORK &amp; SITE PREPARATION</h2>
    <p class="service-text">Depending on the nature of the, it is imperative that your foundation and earth is well prepared for construction and planting. This will determine a quality outcome and the longevity we promote so you don’t have issues in the future.</p>
    <p class="service-text">The Halvorsen group provides the relevant services required so your ground can be covered! This includes, clearing, excavation, levelling, solid foundations and so on. With experience in soft and hard landscape installation and construction, we know that longevity is impacted by solid preparations.</p>
    <p class="service-text">The Halvorsen group manages all excavation and site preparation works for you.</p>
  </section>

  <section class="service-column service-column--install">
    <h2 class="service-heading">INSTALLATION &amp; CONSTRUCTION</h2>
    <p class="service-text">Upon a well prepared site, The Halvorsen group are a professional landscape and construction company that works with a whole range of materials and structural designs.</p>
    <p class="service-text">Browse through our portfolio to see our quality finishes and versatile capabilities including:</p>
    <ul class="capability-list">
      <li>Decking</li>
      <li>Tiling</li>
      <li>Paving</li>
      <li>Pathways</li>
      <li>Irrigation</li>
      <li>Lawn</li>
      <li>Lighting</li>
      <li>Concreting</li>
      <li>Irrigation and<br>Automatic Systems</li>
      <li class="capability--second">Walls and Screening</li>
      <li class="capability--second">Plant supply &amp; Installation</li>
      <li class="capability--second">Covered Structures and Arbours</li>
      <li class="capability--second">Water Features</li>
      <li class="capability--second">Rock features</li>
      <li class="capability--second">Aggregrate designs</li>
      <li class="capability--second">Metal Sculptures</li>
      <li class="capability--second">Pool Paving and Features</li>
    </ul>
    <p class="service-text materials">Just some of the materials we have worked with include Bluestone, Limestone, Hardwood, Aggregate.</p>
  </section>

  <h2 class="display-title display-title--lifestyle">LANDSCAPING TO YOUR LIFESTYLE</h2>

  <svg class="photo-strip photo-strip--bottom" viewBox="0 0 1280 138" preserveAspectRatio="none">
    <g role="img" aria-label="Photo: lit front entrance with timber doors and iron gate"><polygon points="0,0 216,0 210,138 0,138" fill="var(--photo-entrance)"/></g>
    <g role="img" aria-label="Photo: swimming pool with pale stone paving and hedges"><polygon points="224,0 431,0 425,138 218,138" fill="var(--photo-pool)"/></g>
    <g role="img" aria-label="Photo: timber deck with steps and rendered garden walls"><polygon points="438,0 646,0 640,138 432,138" fill="var(--photo-deck)"/></g>
    <g role="img" aria-label="Photo: lawn with stepping pavers and a framed feature planter"><polygon points="654,0 856,0 850,138 648,138" fill="var(--photo-lawn)"/></g>
    <g role="img" aria-label="Photo: garden pavilion and lawn lit at evening"><polygon points="864,0 1068,0 1062,138 858,138" fill="var(--photo-evening)"/></g>
    <g role="img" aria-label="Photo: timber-clad wall with stepping-stone path"><polygon points="1074,0 1280,0 1280,138 1068,138" fill="var(--photo-timber)"/></g>
  </svg>
</main>
</body>
</html>
```